Tolvene Hub Redesign

tolvenehub.com is one of our old, high-traffic multilingual site.

its interface is very old, so we want to redesign it to give a modern, attractive design, with comfortable colors and layout.

beside the current content of the main page we want to add two places for dynamic banners.

The site has an App in iOS and Android, we want an ad in a noticeable place for it.

this ad will be permanent.

the site now has 12 languages, but we may add new languages soon, so design must consider this.

redesign of two internal pages also required:
- the main listing page, example: http://www.tolvenehub.example/en/cat/252
- the article view page: http://www.tolvenehub.example/en/10323

Reason: want to receive more designs ...

```html
<!DOCTYPE html>
<html lang="en">
<head>
<meta charset="utf-8">
<title>Tolvene Hub — Home</title>
<link href="https://fonts.googleapis.com/css2?family=Open+Sans:wght@400;600;700&family=Oswald:wght@500&display=swap" rel="stylesheet">
<style>
  :root{
    --teal:#2b9bab;
    --teal-dark:#1f7d8b;
    --teal-light:#e3f2f4;
    --ink:#3b3b3b;
    --muted:#777;
    --line:#d9e3e5;
    --bg:#ffffff;
    --page:#f3f5f5;
  }
  *{box-sizing:border-box;margin:0;padding:0}
  html,body{width:900px;height:1200px;overflow:hidden;background:var(--bg)}
  body{font-family:"Open Sans",Arial,sans-serif;color:var(--ink);position:relative}
  .page{position:relative;width:900px;height:1200px;overflow:hidden;background:var(--page)}

  /* header */
  .site-header{position:absolute;left:0;top:0;width:900px;height:62px;background:#fff;border-bottom:1px solid var(--line)}
  .brand{position:absolute;left:26px;top:14px;display:flex;align-items:center;gap:8px;font-weight:700;font-size:19px;color:var(--teal-dark)}
  .brand-dot{width:14px;height:14px;border-radius:50%;background:var(--teal)}
  .utility{position:absolute;right:24px;top:6px;display:flex;gap:10px;align-items:center;font-size:10px;color:var(--muted)}
  .lang-select{border:1px solid var(--line);padding:2px 8px}
  .search{width:150px;height:20px;background:var(--teal);color:#fff;font-size:10px;padding:3px 8px;display:flex;justify-content:space-between;align-items:center}
  .main-nav{position:absolute;right:24px;top:34px;display:flex;gap:26px;font-size:12px;color:#555}
  .main-nav .active{color:var(--teal);border-bottom:2px solid var(--teal);padding-bottom:4px}

  /* hero */
  .hero-photo{position:absolute;left:0;top:62px;width:900px;height:400px;background:linear-gradient(100deg,#e9f1f2 0%,#cfd9db 35%,#9b8774 60%,#5b4a3e 100%)}
  .feature{position:absolute;left:0;top:455px;width:900px;height:228px;background:var(--teal)}
  .feature-art{position:absolute;left:34px;top:-28px;width:170px;height:210px;background:linear-gradient(160deg,#d9b27c,#8b5a2b);border-radius:4px}
  .feature-body{position:absolute;left:240px;top:14px;width:630px;color:#fff}
  .feature-title{font-family:"Oswald","Open Sans",sans-serif;font-weight:500;font-size:22px;letter-spacing:.5px;margin-bottom:8px}
  .feature-text{font-size:11px;line-height:16px;opacity:.95}
  .feature-more{display:block;text-align:right;font-size:11px;margin-top:8px;text-decoration:underline}
  .slider-dots{position:absolute;left:0;top:694px;width:900px;display:flex;justify-content:center;gap:8px}
  .slider-dots span{width:9px;height:9px;border-radius:50%;background:#c6d3d5}
  .slider-dots .on{background:var(--teal)}

  /* panels */
  .panel{position:absolute;background:#fff;border:1px solid var(--line)}
  .panel-head{height:30px;background:var(--teal);color:#fff;font-size:13px;font-weight:600;padding:6px 12px}
  .panel-list{list-style:none;padding:8px 12px;font-size:10.5px;line-height:15px}
  .panel-list li{padding:6px 0;border-bottom:1px solid #eef2f3}
  .panel-list li:first-child{color:var(--teal)}
  .panel-more{position:absolute;right:12px;bottom:8px;font-size:10.5px;color:var(--teal-dark);text-decoration:underline}
  .tenets{left:36px;top:738px;width:384px;height:236px}
  .categories{left:474px;top:738px;width:390px;height:250px}
  .files{left:474px;top:1002px;width:390px;height:198px}
  .topic-stack{position:absolute;left:36px;top:988px;width:384px}
  .topic-stack .panel-head{margin-bottom:6px}
  .topic{height:26px;background:var(--teal-light);border-left:4px solid var(--teal);color:var(--teal-dark);font-size:11.5px;padding:5px 12px;margin-bottom:30px}
  .topic-stack .panel-head{margin-bottom:30px}
</style>
</head>
<body>
<div class="page">
  <header class="site-header">
    <div class="brand"><span class="brand-dot"></span>Tolvene Hub</div>
    <div class="utility">
      <span class="lang-select">Language : English ▾</span>
      <span class="search">Search the site
        <svg width="10" height="10" viewBox="0 0 10 10"><circle cx="4" cy="4" r="3" fill="none" stroke="#fff" stroke-width="1.4"/><line x1="6.2" y1="6.2" x2="9" y2="9" stroke="#fff" stroke-width="1.4"/></svg>
      </span>
    </div>
    <nav class="main-nav">
      <span class="active">Home</span><span>Categories</span><span>New Fatwas</span><span>About</span><span>Articles &amp; Books</span><span>Send A Question</span><span>Introduction to Islam</span>
    </nav>
  </header>

  <div class="hero-photo" role="img" aria-label="Banner photograph of a man reading a book"></div>

  <section class="feature">
    <div class="feature-art" role="img" aria-label="Illustration of a parchment scroll and quill labelled New Fatwas"></div>
    <div class="feature-body">
      <h2 class="feature-title">HIS MOTHER MISTREATS HIS WIFE AND HER FAMILY.</h2>
      <p class="feature-text">My wife is suffering because of my mother's treatment of her. She says hurtful words to her and treats her family with no justification other than thinking badly of them, and this treatment even extends to my wife's family. My mother has started to make inappropriate and untrue accusations against my wife to my wife's family, so my wife has cut off all ties with my mother. Please note that my wife has been patient in putting up with my mother's treatment of her for several years, until she could bear it no longer. What should I do to reconcile between them while keeping ties with my mother?</p>
      <span class="feature-more">Read More</span>
    </div>
  </section>
  <div class="slider-dots"><span></span><span></span><span></span><span class="on"></span><span></span><span></span></div>

  <section class="panel tenets">
    <div class="panel-head">Basic Tenets of Faith</div>
    <ul class="panel-list">
      <li>How should she advise her sister, who keeps her daughter away from another wife, and he has a son from her, and he is confused as to how he should deal with her.</li>
      <li>A woman asking for a divorce from her husband who is addicted to drugs.</li>
      <li>He did the marriage contract with her and was intimate with her without intercourse in Ramadan, and he had intercourse with her before announcing the marriage.</li>
    </ul>
    <span class="panel-more">Read More</span>
  </section>

  <section class="topic-stack">
    <div class="panel-head">The Muslim Woman</div>
    <div class="topic">Jurisprudence Acts of Worships</div>
    <div class="topic">Counselling</div>
    <div class="topic">Contemporary Transactions</div>
    <div class="topic">Jurisprudence of Muslim Minorities</div>
  </section>

  <section class="panel categories">
    <div class="panel-head">Categories</div>
    <ul class="panel-list">
      <li>Basic Tenets of Faith</li>
      <li>The Qur'aan and its Sciences</li>
      <li>Hadeeth &amp; its Sciences</li>
      <li>Rulings on Jihad – Fiqh of the family</li>
      <li>Islamic History and Biography</li>
      <li>Enjoining what is good and forbidding what is evil</li>
    </ul>
    <span class="panel-more">Read More</span>
  </section>

  <section class="panel files">
    <div class="panel-head">Files</div>
    <ul class="panel-list">
      <li>The virtue of fasting Ramadan</li>
      <li>prohibition on songs and music</li>
      <li>Welcoming Ramadan</li>
      <li>Rulings on zakaah, the eid and Hajj</li>
      <li>Paradise &amp; Hell</li>
    </ul>
    <span class="panel-more">Read More</span>
  </section>
</div>
</body>
</html>
```